Business Card Design Project for - The Pellowick Greenworks Company Ltd. We are a Landscape and garden

I would like designer to use all special glosses etc so i can have a professional looking business card. The theme of the business card can reflect that of the Logo attached by MarkQuarry or your own unique ideas.. please feel free to go wild as i hope i can select a winner i like - my budget will be committed so please get involved. Good luck and thank you Lyndon

Target Market(s)

Must look Professional

General Public and Businesses including Councils, Local Government, Hospitals, Hotels, Professionals and Professional Sports People.

Industry/Entity Type

Landscape Gardening

Contact Information for Business Card

The Pellowick Greenworks Company Ltd

Mr L.R Ashcombe
Head Office - Quayfront Park Manchester
t. 0772 408 916
e. info@pellowickgreenworks.co.uk
w. www.pellowickgreenworks.co.uk

Facebook - https://www.friendpage-example.com/ThePellowickGreenworksCompany/
Twitter - https://chirpline-example.com/ThePruningCart
Instagram - https://www.snapgrid-example.com/thepellowickgreenworkscompany/?hl=en
Google+ - https://circles.searchhub-example.com/u/0/208473950162438571093
Yelp - https://www.reviewnook-example.co.uk/biz/the-pellowick-greenworks-company-manchester-4

Font styles to use
Serif
Script
Other font styles liked:
• I don't have much of an idea of font types sorry

Colors

Designer to choose colors to be used in the design.

Requirements
Must have
• A Professional look and Design
• Special effects with gloss and fading of colours possibly..
• Front and back design
Nice to have
• All special features with effects and gloss etc

```html
<!DOCTYPE html>
<html lang="en">
<head>
<meta charset="utf-8">
<title>The Pellowick Greenworks Company Ltd – Business Card</title>
<link rel="stylesheet" href="https://fonts.googleapis.com/css2?family=Open+Sans:wght@400;600;700&display=swap">
<style>
  :root {
    --page-bg: #e9e6e1;
    --card-black: #0b0b0b;
    --card-white: #fbfbfb;
    --leaf-green: #5cbf2a;
    --leaf-green-light: #8fd63c;
    --ink-dark: #2c2c2c;
    --ink-grey: #7d7d7d;
    --swoosh-grey: #9a9a9c;
    --social-text: #d6d6d6;
  }
  * { box-sizing: border-box; margin: 0; padding: 0; }
  html, body { width: 1200px; height: 900px; overflow: hidden; }
  body {
    background: var(--page-bg);
    font-family: "Open Sans", Arial, sans-serif;
    display: flex;
    align-items: center;
    justify-content: center;
    gap: 30px;
  }
  .card {
    position: relative;
    width: 560px;
    height: 320px;
    border-radius: 3px;
    overflow: hidden;
    box-shadow: 0 6px 18px rgba(0,0,0,0.22);
  }

  /* Back */
  .card--back { background: var(--card-black); }
  .social-list {
    position: absolute;
    left: 34px;
    top: 118px;
    list-style: none;
  }
  .social-list li {
    display: flex;
    align-items: center;
    gap: 9px;
    height: 21px;
    font-size: 11px;
    color: var(--social-text);
    white-space: nowrap;
  }
  .social-dot {
    width: 13px; height: 13px;
    border-radius: 50%;
    background: var(--leaf-green);
    flex: none;
  }

  /* Front */
  .card--front {
    background: linear-gradient(160deg, #ffffff 0%, var(--card-white) 55%, #f1f1f1 100%);
  }
  .holder {
    position: absolute;
    left: 40px;
    top: 92px;
  }
  .holder__name {
    font-size: 19px;
    font-weight: 700;
    color: var(--leaf-green);
    letter-spacing: 0.2px;
    line-height: 1.1;
  }
  .holder__office {
    font-size: 14.5px;
    color: var(--ink-dark);
    line-height: 1.3;
  }
  .brand {
    position: absolute;
    right: 34px;
    top: 70px;
    display: flex;
    align-items: center;
    gap: 10px;
  }
  .brand__dot {
    width: 34px; height: 34px;
    border-radius: 50%;
    background: var(--leaf-green);
    flex: none;
  }
  .brand__name {
    font-size: 14px;
    font-weight: 600;
    color: var(--ink-grey);
    line-height: 1.25;
    text-transform: uppercase;
    letter-spacing: 1px;
    width: 190px;
  }
  .contact-list {
    position: absolute;
    left: 40px;
    top: 188px;
    list-style: none;
  }
  .contact-list li {
    display: flex;
    align-items: center;
    gap: 8px;
    height: 22px;
    font-size: 14.5px;
    color: var(--ink-dark);
  }
  .contact-icon { width: 12px; height: 12px; flex: none; }
  .card__wave {
    position: absolute;
    left: 0; bottom: 0;
    width: 560px; height: 320px;
    pointer-events: none;
  }
</style>
</head>
<body>

  <section class="card card--back" aria-label="Business card back">
    <ul class="social-list">
      <li><span class="social-dot"></span>www.friendpage-example.com/ThePellowickGreenworksCompany/</li>
      <li><span class="social-dot"></span>www.chirpline-example.com/ThePruningCart</li>
      <li><span class="social-dot"></span>www.snapgrid-example.com/thepellowickgreenworkscompany/?hl=en</li>
      <li><span class="social-dot"></span>www.circles.searchhub-example.com/u/0/208473950162438571093</li>
      <li><span class="social-dot"></span>www.reviewnook-example.co.uk/biz/the-pellowick-greenworks-company-manchester-4</li>
    </ul>
  </section>

  <section class="card card--front" aria-label="Business card front">
    <svg class="card__wave" viewBox="0 0 560 320" aria-hidden="true">
      <defs>
        <linearGradient id="greenFade" x1="0" y1="1" x2="1" y2="0">
          <stop offset="0" stop-color="#4fb322"/>
          <stop offset="1" stop-color="#8fd63c"/>
        </linearGradient>
      </defs>
      <path d="M0,250 C130,262 300,220 430,170 C480,150 520,140 560,136 L560,140 C500,150 440,180 360,218 C250,268 120,282 0,272 Z" fill="var(--swoosh-grey)"/>
      <path d="M0,292 C140,300 300,262 420,205 C480,176 520,160 560,152 L560,320 L0,320 Z" fill="url(#greenFade)"/>
    </svg>

    <div class="holder">
      <p class="holder__name">MR L.R ASHCOMBE</p>
      <p class="holder__office">Head Office - Quayfront Park Manchester</p>
    </div>

    <div class="brand">
      <span class="brand__dot"></span>
      <p class="brand__name">The Pellowick Greenworks Company Ltd</p>
    </div>

    <ul class="contact-list">
      <li>
        <svg class="contact-icon" viewBox="0 0 12 12" aria-hidden="true"><path d="M2.5 1 L4.5 1 L5.2 3.6 L3.9 4.6 C4.5 6 5.8 7.4 7.4 8.1 L8.4 6.8 L11 7.5 L11 9.5 C11 10.4 10.3 11 9.5 11 C5 10.6 1.4 7 1 2.5 C1 1.7 1.6 1 2.5 1 Z" fill="var(--leaf-green)"/></svg>
        0772 408 916
      </li>
      <li>
        <svg class="contact-icon" viewBox="0 0 12 12" aria-hidden="true"><rect x="0.5" y="2" width="11" height="8" fill="var(--leaf-green)"/><path d="M0.8 2.4 L6 6.6 L11.2 2.4" fill="none" stroke="#fff" stroke-width="1"/></svg>
        info@pellowickgreenworks.co.uk
      </li>
      <li>
        <svg class="contact-icon" viewBox="0 0 12 12" aria-hidden="true"><circle cx="6" cy="6" r="5.5" fill="var(--leaf-green)"/><path d="M0.8 6 H11.2 M6 0.6 C3.8 3 3.8 9 6 11.4 M6 0.6 C8.2 3 8.2 9 6 11.4" fill="none" stroke="#fff" stroke-width="0.8"/></svg>
        www.pellowickgreenworks.co.uk
      </li>
    </ul>
  </section>

</body>
</html>
```